Local Restaurant Website Design

We are working with a Restaurant in California. They serve BBQ chicken, ribs, and other American cuisine. Plus catering.

Here are a few websites we found for inspiration:
https://www.marigoldsmokepit.com
https://www.brambletable.com/home
https://ravellitrattoria.com
https://www.tortugayard.com
https://www.pablitos.com
https://elfarolitokitchen.com
https://www.solymarburritohut.com

Thank you for taking the time to consider designing a website for us. We are web developers based in Stockton, CA, USA. Most of our projects go through the same process. Understanding this process may help you win a project with us. We custom-code all of our websites in-house. We don’t have any requirements as to what tools you use for your design, but we ask that you follow these guidelines.

IMAGES:
If you use any images or icons in the design, we ask that you have a link to the asset so we can purchase the image/icon. Most of the designs we submit do not have the customer’s images on them unless they have some great images. Be creative; show us the feeling you are trying to portray with your image choices. Use any royalty-free site you choose. We subscribe to Norvex and mainly use their images, but we can purchase images outside of Norvex. PLEASE NOTE: we will not submit designs to clients with watermarks on the images.

FONTS:
We ask that you identify the fonts you’re using in the design. This can be done in a message if you want. We typically use Palmora Fonts and Norvex Fonts.

CONTENT:
We're always open to different content and ideas. We often submit designs with stock images so the client can see our vision. We typically take pictures after the website launch to use their images with our vision. Lorem Ipsum is fine for paragraphs, but we ask that you make the Headers with correct English. We want to be able to show the vision and identify the sections of the website.

INSPIRATION:
We typically add a couple of links in the brief of websites we like to help you get started in your design.

REVISIONS:
We do not often ask for revisions of the designs unless we see something in the design that may not appeal to the client. If there are slight changes that we want to make, we do that in the development process.

FEEDBACK:
We rarely give feedback on designs during the design process. We are working on many website projects and do not have the time to provide feedback. We usually respond if your request is well thought out and asks specific questions, but a note asking “feedback, please” usually goes unanswered.

```html
<!DOCTYPE html>
<html lang="en">
<head>
<meta charset="utf-8">
<title>Ember Coop — BBQ Chicken &amp; Catering</title>
<link rel="stylesheet" href="https://fonts.googleapis.com/css2?family=IBM+Plex+Sans:wght@500;600;700&family=Josefin+Sans:wght@400;500;600&display=swap">
<style>
:root{
  --ink:#1d1d1d;
  --muted:#444;
  --white:#ffffff;
  --cream:#fdf5cc;
  --soft:#f6f4f4;
  --yellow:#f1e51c;
  --orange:#ef963f;
  --flame:#ee5526;
  --footer:#e0520e;
  --price:#f2b91a;
  --rule:#f07a52;
}
*{box-sizing:border-box;margin:0;padding:0}
html,body{width:1200px;height:4384px;overflow:hidden;background:var(--white)}
body{font-family:"Josefin Sans",sans-serif;color:var(--ink)}
.page{position:relative;width:1200px;height:4384px;overflow:hidden}
.abs{position:absolute}
.ph{position:absolute}
.heading{font-family:"IBM Plex Sans",sans-serif;font-weight:700}
.brush{position:absolute;background:var(--yellow);display:flex;align-items:center;justify-content:center;
  font-family:"IBM Plex Sans",sans-serif;font-weight:700;font-size:16px;color:var(--ink);
  clip-path:polygon(2% 18%,12% 8%,40% 14%,70% 4%,97% 12%,92% 30%,100% 48%,94% 64%,99% 84%,70% 92%,40% 86%,8% 96%,4% 78%,0 56%,5% 38%)}
.para{font-size:12px;line-height:1.18;color:var(--muted)}

/* hero */
.hero{left:0;top:0;width:1200px;height:621px;background:radial-gradient(circle at 70% 45%,#a8441c 0,#6b2a12 40%,#2a120a 100%)}
.hero-top{left:0;top:0;width:1200px;height:86px;background:rgba(120,110,110,.55)}
.nav{left:216px;top:31px;width:768px;height:126px;background:var(--white);border-radius:63px}
.nav a{position:absolute;top:52px;font-size:15px;font-weight:500;color:var(--ink);text-decoration:none;white-space:nowrap}
.nav a.active{color:var(--flame)}
.brand{position:absolute;left:244px;top:52px;width:150px;text-align:center;white-space:nowrap;font-family:"IBM Plex Sans",sans-serif;font-weight:700;font-size:20px;line-height:20px;color:var(--flame)}
.hero-title{left:185px;top:268px;font-size:41px;line-height:54px;letter-spacing:2px;color:var(--white);white-space:nowrap}
.plate{left:871px;top:437px;width:279px;height:279px;border-radius:50%;background:radial-gradient(circle,#8a4a2c 0,#b0613a 35%,#f3f0ec 62%);box-shadow:0 8px 20px rgba(0,0,0,.3)}

/* about */
.tomatoes{left:0;top:621px;width:184px;height:180px;background:radial-gradient(circle at 40% 40%,#e0321d 0,rgba(224,50,29,.2) 60%,transparent 75%)}
.taco{left:182px;top:672px;width:376px;height:238px;background:radial-gradient(ellipse at 50% 55%,#d9a441 0,#b87a32 40%,#f4f1ea 70%)}
.about-title{left:599px;top:688px;font-size:24px;font-weight:600}
.about-text{left:599px;top:735px;width:404px}

/* offer */
.offer{left:0;top:984px;width:1200px;height:684px;background:var(--cream)}
.eyebrow{left:0;top:1046px;width:1200px;text-align:center;font-size:13px;letter-spacing:1px}
.offer-title{left:0;top:1072px;width:1200px;text-align:center;font-size:24px;font-weight:600}
.offer-text{left:440px;top:1110px;width:320px;text-align:center;font-size:10.5px}
.card-label{position:absolute;text-align:center;font-family:"IBM Plex Sans",sans-serif;font-weight:500;font-size:18px}
.card-link{position:absolute;text-align:center;font-size:13px;color:var(--ink)}
.card-link.hot{color:var(--flame);text-decoration:underline}

/* video */
.video{left:0;top:1668px;width:659px;height:332px;background:var(--orange)}
.video-deco{left:0;top:1668px;width:170px;height:162px;background:radial-gradient(circle at 40% 40%,rgba(220,60,30,.7) 0,rgba(239,150,63,0) 70%)}
.video-title{left:211px;top:1744px;font-size:24px;font-weight:500;color:var(--white)}
.video-text{left:211px;top:1784px;width:330px;color:var(--white);font-size:11px}
.thumb{position:absolute;top:1877px;width:72px;height:48px;background:linear-gradient(135deg,#2b1a12,#c0622a 60%,#3a2414)}
.tv{left:592px;top:1685px;width:417px;height:298px;border-radius:14px;background:linear-gradient(160deg,#e9e9e9,#bdbdbd)}
.tv-screen{left:612px;top:1703px;width:300px;height:252px;border-radius:22px;background:radial-gradient(circle at 50% 70%,#7a3a1c 0,#1e1511 70%)}

/* bbq banner */
.bbq{left:0;top:2000px;width:1200px;height:274px;background:linear-gradient(90deg,#2f3436 0,#3a3d3e 45%,#6b3216 62%,#8c4a1e 100%)}
.bbq-title{left:187px;top:2064px;font-size:28px;line-height:36px;font-weight:600;color:var(--white)}

/* menu */
.menu{left:0;top:2274px;width:1200px;height:594px;background:var(--soft)}
.menu-title{left:0;top:2324px;width:1200px;text-align:center;font-size:30px;font-weight:600}
.tabs{left:0;top:2382px;width:1200px;display:flex;justify-content:center;gap:22px;font-size:13px;letter-spacing:.5px}
.tabs span.dot{color:var(--orange)}
.tabs .on{border-bottom:3px double var(--rule);padding-bottom:5px}
.dish{position:absolute;width:400px;height:68px}
.dish .pic{position:absolute;left:0;top:0;width:68px;height:68px;background:linear-gradient(135deg,#4a3020,#b47a44 55%,#e7d9bf)}
.dish .name{position:absolute;left:77px;top:6px;font-family:"IBM Plex Sans",sans-serif;font-weight:600;font-size:18px;white-space:nowrap}
.dish .line{position:absolute;top:13px;height:5px;border-top:1px solid var(--rule);border-bottom:1px solid var(--rule)}
.dish .price{position:absolute;top:5px;font-family:"IBM Plex Sans",sans-serif;font-weight:600;font-size:18px;color:var(--price)}
.dish .desc{position:absolute;left:77px;top:32px;width:260px;font-size:11px;line-height:1.15;color:var(--muted)}
.board{left:958px;top:2672px;width:242px;height:192px;background:radial-gradient(ellipse at 50% 55%,#6b3a22 0,#c98d52 38%,#f3ede4 70%)}

/* process */
.process{left:0;top:2868px;width:1200px;height:264px;background:radial-gradient(ellipse at 50% 40%,#4a3a26 0,#262320 55%,#151413 100%)}
.process-title{left:0;top:2966px;width:1200px;text-align:center;font-size:36px;font-weight:600;color:var(--white)}
.process-text{left:0;top:3021px;width:1200px;text-align:center;font-size:14px;color:var(--white)}

/* gallery */
.gallery{left:0;top:3132px;width:1200px;height:752px;background:linear-gradient(180deg,#f3f3f3,#fafafa)}
.gallery-title{left:187px;top:3250px;font-size:37px;font-weight:700}
.gallery-text{left:187px;top:3310px;width:360px;font-size:11px}
.shot{position:absolute}

/* contact */
.contact{left:0;top:3884px;width:1200px;height:189px;background:var(--orange)}
.icon{position:absolute;top:3944px;width:63px;height:63px}
.c-label{position:absolute;font-family:"IBM Plex Sans",sans-serif;font-weight:600;font-size:13px;color:var(--white)}
.c-value{position:absolute;font-family:"IBM Plex Sans",sans-serif;font-weight:500;font-size:15px;color:var(--white);line-height:1.25}

/* footer */
.footer{left:0;top:4073px;width:1200px;height:311px;background:var(--footer)}
.footer-brand{left:0;top:4146px;width:1200px;text-align:center;font-family:"IBM Plex Sans",sans-serif;font-weight:700;font-size:34px;color:var(--white)}
.socials{left:0;top:4236px;width:1200px;display:flex;justify-content:center;gap:16px}
.socials span{width:16px;height:16px;border-radius:50%;background:var(--white)}
.hours{left:0;top:4272px;width:1200px;text-align:center;font-size:14px;color:var(--white)}
.f-links{left:0;top:4306px;width:1200px;display:flex;justify-content:center;gap:30px;font-size:14px;color:var(--white)}
.f-rule{left:0;top:4340px;width:1200px;height:1px;background:rgba(255,255,255,.6)}
.copy{left:0;top:4357px;width:1200px;text-align:center;font-size:11px;color:var(--white)}
</style>
</head>
<body>
<div class="page">

  <!-- Hero -->
  <div class="ph hero" role="img" aria-label="Chicken drumsticks grilling over flames"></div>
  <div class="abs hero-top"></div>
  <nav class="abs nav">
    <a class="active" style="left:31px">Home</a>
    <a style="left:95px">About Us</a>
    <a style="left:186px">Menu</a>
    <span class="brand">Ember Coop</span>
    <a style="left:453px">Catering</a>
    <a style="left:543px">Find Restaurant</a>
    <a style="left:690px">Log In</a>
  </nav>
  <h1 class="abs heading hero-title">Flame-Grilled Chicken<br>Made Fresh Daily</h1>
  <div class="brush" style="left:190px;top:391px;width:218px;height:55px;justify-content:flex-start;padding-left:35px">Oder Now</div>
  <div class="ph plate" role="img" aria-label="Plate of grilled steak with fresh salad"></div>

  <!-- About -->
  <div class="ph tomatoes" role="img" aria-label="Scattered tomato slices"></div>
  <div class="ph taco" role="img" aria-label="Loaded beef taco with lettuce and cheese"></div>
  <h2 class="abs heading about-title">About Us</h2>
  <p class="abs para about-text">It is a long established fact that a reader will be distracted by the readable content of a page when looking at its layout. The point of using Lorem Ipsum is that it has a more-or-less normal distribution of letters, as opposed to using 'Content here, content here', making it look like readable English.It is a long established fact that a reader will be readable content of a page when looking at its layout. The point of using Lorem Ipsum is that it has a more-or-less normal distribution of letters, as opposed to using 'Content here, content here', making it look like readable English.</p>
  <div class="brush" style="left:602px;top:868px;width:214px;height:51px;font-size:14px;justify-content:flex-start;padding-left:32px">Learn More</div>

  <!-- Offer -->
  <div class="abs offer"></div>
  <p class="abs eyebrow">FLAVORS FOR ROYALTY</p>
  <h2 class="abs heading offer-title">We Offer Top Notch</h2>
  <p class="abs para offer-text">Lorem Ipsum is simply dummy text of the printing and typesetting industry. Lorem Ipsum has been the industry's standard dummy text ever since the 1500s,</p>

  <div class="ph" style="left:187px;top:1157px;width:254px;height:337px;background:linear-gradient(160deg,#2a2623,#6b5a44 55%,#d79a3a)" role="img" aria-label="Breakfast plate with eggs, sausages and croissants"></div>
  <p class="card-label" style="left:187px;top:1506px;width:254px">Breakfast</p>
  <p class="card-link hot" style="left:187px;top:1542px;width:254px">View All</p>

  <div class="ph" style="left:473px;top:1203px;width:252px;height:337px;background:radial-gradient(circle at 50% 45%,#6a3a1e 0,#262322 55%,#141313)" role="img" aria-label="Grilled chicken wing on a fork"></div>
  <p class="card-label" style="left:473px;top:1551px;width:252px">Appetizers</p>
  <p class="card-link" style="left:473px;top:1588px;width:252px">View All</p>

  <div class="ph" style="left:757px;top:1157px;width:254px;height:337px;background:radial-gradient(circle at 50% 45%,#a02834 0,#2a2826 50%,#141414)" role="img" aria-label="Red cocktail in a coupe glass"></div>
  <p class="card-label" style="left:757px;top:1505px;width:254px">Drinks</p>
  <p class="card-link" style="left:757px;top:1542px;width:254px">View All</p>

  <!-- Video -->
  <div class="abs video"></div>
  <div class="ph video-deco" role="img" aria-label="Scattered fresh ingredients"></div>
  <h2 class="abs video-title">VIDEO OF THE WEEK</h2>
  <p class="abs para video-text">Lorem Ipsum is simply dummy text of the printing and typesetting industry. Lorem Ipsum has been the industry's standard dummy text ever since the 1500s, when an unknown printer took a galley of type and scrambled it to make a type specimen book.</p>
  <div class="thumb" style="left:206px" role="img" aria-label="Video thumbnail: grilled dish"></div>
  <div class="thumb" style="left:287px" role="img" aria-label="Video thumbnail: table spread"></div>
  <div class="thumb" style="left:368px" role="img" aria-label="Video thumbnail: flame grill"></div>
  <div class="thumb" style="left:448px" role="img" aria-label="Video thumbnail: roasted meat"></div>
  <svg class="abs" style="left:529px;top:1894px" width="10" height="14" viewBox="0 0 10 14"><path d="M2 1l6 6-6 6" fill="none" stroke="#fff" stroke-width="1.5"/></svg>
  <div class="ph tv" role="img" aria-label="Retro television showing sauce poured over grilled meat"></div>
  <div class="ph tv-screen"></div>
  <svg class="abs" style="left:738px;top:1813px" width="52" height="56" viewBox="0 0 52 56"><path d="M4 2l46 26-46 26z" fill="rgba(255,255,255,.85)"/></svg>

  <!-- BBQ banner -->
  <div class="ph bbq" role="img" aria-label="Glazed BBQ chicken wings with a basting brush"></div>
  <h2 class="abs heading bbq-title">Enjoy The Taste Of Our<br>BBQ Chicken</h2>
  <div class="brush" style="left:190px;top:2158px;width:214px;height:50px;font-size:15px;justify-content:flex-start;padding-left:44px">Order Now</div>

  <!-- Menu -->
  <div class="abs menu"></div>
  <h2 class="abs heading menu-title">Delicious Menu</h2>
  <div class="abs tabs"><span class="on">MORNING</span><span class="dot">•</span><span>WEEKDAY LUNCH</span><span class="dot">•</span><span>DINNER</span><span class="dot">•</span><span>WINES</span></div>

  <div class="dish" style="left:187px;top:2459px"><div class="pic" role="img" aria-label="Fajita tacos"></div><span class="name">Fajitas Taccos</span><span class="line" style="left:210px;width:116px"></span><span class="price" style="left:337px">$09.00</span><p class="desc">Lorem Ipsum has been the industry's standard dummy text ever since the 1500s, when an</p></div>
  <div class="dish" style="left:187px;top:2546px"><div class="pic" role="img" aria-label="Jerky burger"></div><span class="name">Jerky Burger</span><span class="line" style="left:200px;width:116px"></span><span class="price" style="left:326px">$09.00</span><p class="desc">Lorem Ipsum has been the industry's standard dummy text ever since the 1500s, when an</p></div>
  <div class="dish" style="left:187px;top:2633px"><div class="pic" role="img" aria-label="Pot roast"></div><span class="name">Pot Roast</span><span class="line" style="left:172px;width:116px"></span><span class="price" style="left:298px">$09.00</span><p class="desc">Lorem Ipsum has been the industry's standard dummy text ever since the 1500s, when an</p></div>

  <div class="dish" style="left:625px;top:2459px"><div class="pic" role="img" aria-label="Cobb salad"></div><span class="name">Cob Salad</span><span class="line" style="left:175px;width:116px"></span><span class="price" style="left:302px">$09.00</span><p class="desc">Lorem Ipsum has been the industry's standard dummy text ever since the 1500s, when an</p></div>
  <div class="dish" style="left:625px;top:2546px"><div class="pic" role="img" aria-label="Cheesecake slice"></div><span class="name">Cheese Cake</span><span class="line" style="left:198px;width:116px"></span><span class="price" style="left:325px">$09.00</span><p class="desc">Lorem Ipsum has been the industry's standard dummy text ever since the 1500s, when an</p></div>
  <div class="dish" style="left:625px;top:2633px"><div class="pic" role="img" aria-label="Tacos"></div><span class="name">Tacos</span><span class="line" style="left:135px;width:116px"></span><span class="price" style="left:262px">$09.00</span><p class="desc">Lorem Ipsum has been the industry's standard dummy text ever since the 1500s, when an</p></div>

  <div class="brush" style="left:494px;top:2749px;width:212px;height:51px;font-size:15px">View all</div>
  <div class="ph board" role="img" aria-label="Grilled steak on a wooden board"></div>

  <!-- Process -->
  <div class="ph process" role="img" aria-label="Meat on the grill with tongs"></div>
  <h2 class="abs heading process-title">Our BBQ Proccess</h2>
  <p class="abs process-text">Lorem Ipsum is simply dummy text of the printing and typesetting industry.</p>

  <!-- Gallery -->
  <div class="abs gallery"></div>
  <h2 class="abs heading gallery-title">Our Gallery</h2>
  <p class="abs para gallery-text">It is a long established fact that a reader will be distracted by the readable content of a page when looking at its layout.</p>
  <div class="brush" style="left:187px;top:3358px;width:160px;height:36px;font-size:14px;justify-content:flex-start;padding-left:34px">View All</div>

  <div class="shot" style="left:625px;top:3195px;width:177px;height:226px;background:linear-gradient(180deg,#4a3a30,#8a7868 60%,#d9cfc4)" role="img" aria-label="Banquet hall set for an event"></div>
  <div class="shot" style="left:812px;top:3339px;width:197px;height:289px;background:linear-gradient(180deg,#c8c3bd,#f1efed 55%,#d99a60)" role="img" aria-label="Waiter holding a plated dish"></div>
  <div class="shot" style="left:555px;top:3429px;width:247px;height:184px;background:radial-gradient(circle at 50% 50%,#e06a3a 0,#6c9a3a 45%,#f2efe8 80%)" role="img" aria-label="Shrimp and basil dish"></div>
  <div class="shot" style="left:346px;top:3537px;width:201px;height:148px;background:linear-gradient(135deg,#3a2418,#9c4a1e 55%,#2a1a12)" role="img" aria-label="Glazed ribs"></div>
  <div class="shot" style="left:555px;top:3625px;width:206px;height:167px;background:linear-gradient(180deg,#1e1a18,#8a5a2a 55%,#d6a04a)" role="img" aria-label="Buffet trays of food"></div>
  <div class="shot" style="left:771px;top:3625px;width:230px;height:129px;background:linear-gradient(180deg,#f3eef0,#d86a8a 60%,#f7f2f4)" role="img" aria-label="Decorated event tables"></div>
  <div class="shot" style="left:235px;top:3693px;width:311px;height:131px;background:linear-gradient(135deg,#f1ece6,#a8401a 40%,#5e2410 75%,#e9e2d9)" role="img" aria-label="Glazed chicken wings on a board"></div>

  <!-- Contact -->
  <div class="abs contact"></div>
  <svg class="abs" style="left:0;top:3876px" width="1200" height="14" viewBox="0 0 1200 14" preserveAspectRatio="none"><path d="M0 8 Q10 0 20 8 T40 8 T60 8 T80 8 T100 8 T120 8 T140 8 T160 8 T180 8 T200 8 T220 8 T240 8 T260 8 T280 8 T300 8 T320 8 T340 8 T360 8 T380 8 T400 8 T420 8 T440 8 T460 8 T480 8 T500 8 T520 8 T540 8 T560 8 T580 8 T600 8 T620 8 T640 8 T660 8 T680 8 T700 8 T720 8 T740 8 T760 8 T780 8 T800 8 T820 8 T840 8 T860 8 T880 8 T900 8 T920 8 T940 8 T960 8 T980 8 T1000 8 T1020 8 T1040 8 T1060 8 T1080 8 T1100 8 T1120 8 T1140 8 T1160 8 T1180 8 T1200 8 V14 H0Z" fill="#ef963f"/></svg>

  <svg class="icon" style="left:187px" viewBox="0 0 63 63"><circle cx="31.5" cy="31.5" r="29.5" fill="none" stroke="#fff" stroke-width="2.5"/><path d="M21 18c3-3 5-2 7 1l3 5c1 2 0 4-2 5l-2 1c2 5 5 8 10 10l1-2c1-2 3-3 5-2l5 3c3 2 4 4 1 7-4 4-9 4-16-2-8-6-13-13-14-18 0-3 0-6 2-8z" fill="none" stroke="#fff" stroke-width="2.2" stroke-linejoin="round"/></svg>
  <p class="c-label" style="left:260px;top:3947px">Phone Number</p>
  <p class="c-value" style="left:260px;top:3973px">+15550193472</p>

  <svg class="icon" style="left:436px" viewBox="0 0 63 63"><circle cx="31.5" cy="31.5" r="29.5" fill="none" stroke="#fff" stroke-width="2.5"/><rect x="17" y="21" width="29" height="21" rx="2" fill="none" stroke="#fff" stroke-width="2.2"/><path d="M18 23l13.5 10L45 23" fill="none" stroke="#fff" stroke-width="2.2"/></svg>
  <p class="c-label" style="left:507px;top:3943px;font-size:12px">Our&nbsp; Email Address</p>
  <p class="c-value" style="left:507px;top:3968px">info@embercoop.com</p>

  <svg class="abs" style="left:703px;top:3938px" width="62" height="66" viewBox="0 0 62 66"><path d="M31 46C22 35 17 28 17 21a14 14 0 0 1 28 0c0 7-5 14-14 25z" fill="#fff"/><circle cx="31" cy="21" r="5" fill="#ef963f"/><ellipse cx="31" cy="52" rx="27" ry="9" fill="none" stroke="#fff" stroke-width="2.2"/></svg>
  <p class="c-label" style="left:774px;top:3936px;font-size:12px">Our Address</p>
  <p class="c-value" style="left:774px;top:3962px;width:260px">418 Harlow Avenue, Stockton CA 95204</p>

  <!-- Footer -->
  <div class="abs footer"></div>
  <p class="abs footer-brand">Ember Coop</p>
  <div class="abs socials"><span></span><span></span><span></span><span></span></div>
  <p class="abs hours">Mon-sat -07:30AM-12:00AM</p>
  <div class="abs f-links"><span>Home</span><span>Contact</span><span>About Us</span><span>Menu</span><span>Find Restuarent</span></div>
  <div class="abs f-rule"></div>
  <p class="abs copy">Copyright © 2023. EmberCoop. All rights reserved.</p>

</div>
</body>
</html>
```